Flyer to be utilised on social media and email marketing - Making Divorce Applications Affordable

Finalising Your Divorce Made Easy <br/><br/>Are you separated and both seeking to Divorce? At Marrick & Dace Legal we provide a cost effective way for this to occur.... <br/><br/>OLD APPROACH <br/> Arrange a meeting with a solicitor <br/> Attend appointment <br/> Provide background information to the lawyer <br/> Lawyer to draft document <br/> Lawyer to contact you to obtain further instructions, if required <br/>Lawyer to amend divorce application, if further amendments required <br/> Lawyer to send you a copy of the draft Divorce Application<br/>Lawyer to make further changes, if required <br/>Lawyer to resend you draft Divorce Application, if required <br/>Lawyer to organise an appointment to attend office to sign Divorce Application <br/>TIME CONSUMING & COSTLY - CAN COST OVER $3500 <br/><br/>NEW APPROACH <br/> We send you a Form <br/> You complete the Form <br/> We review your instructions <br/>We provide you with advicee <br/>We draft Divorce Application and send to you for review <br/> QUICK & SIMPLE PROCESS - FIXED COST OF $799 INCLUSIVE OF GST <br/><br/>Please include the OLD APPROACH ON THE LEFT SIDE AND NEW APPROACH ON THE RIGHT SIDE OF THE PAGE (SO THAT THEY ARE NEXT TO EACH OTHER)<br/><br/>*Terms and Conditions - Applies to simple joint divorce applications, no court appearances, no drafting or finalising any further court documentations, and excludes disbursements costs including court filing fee <br/>

Target Market(s)

Separated Families - Individuals from 35+

Industry/Entity Type

Legal

Font styles to use
Serif

Colors
0255a3

Requirements
Must have
• Please include website - www.marrickanddacelegal.com.au
• Email - office@marrickanddacelegal.com.au
• Logo Colour - Royal blue colour #10416a or hex code #063169

```html
<!DOCTYPE html>
<html lang="en">
<head>
<meta charset="utf-8">
<title>Marrick &amp; Dace Legal – Finalising Your Divorce Made Easy</title>
<link rel="stylesheet" href="https://fonts.googleapis.com/css2?family=Cinzel:wght@400;500&family=Montserrat:wght@400;500&family=Open+Sans:wght@700&display=swap">
<style>
  :root {
    --brand-blue: #0b4a8c;
    --brand-blue-deep: #063169;
    --brand-blue-light: #5d8db8;
    --panel-blue: #0d4c88;
    --accent-orange: #f0a22a;
    --ink: #1e1e1e;
    --paper: #ffffff;
    --backdrop: #e6e6e6;
  }
  * { box-sizing: border-box; margin: 0; padding: 0; }
  html, body {
    width: 1200px; height: 900px; overflow: hidden;
    background: var(--backdrop);
  }
  .flyer {
    position: absolute; left: 290px; top: 15px;
    width: 620px; height: 870px;
    background: var(--paper);
    overflow: hidden;
    box-shadow: 0 12px 30px rgba(0,0,0,0.18);
  }
  .masthead {
    position: absolute; left: 0; top: 0; width: 620px; height: 81px;
    background: linear-gradient(90deg, var(--brand-blue-deep) 0%, var(--brand-blue) 55%, var(--brand-blue-light) 100%);
    display: flex; align-items: center; justify-content: center;
  }
  .brand-name {
    font-family: "Cinzel", serif; font-weight: 400;
    color: var(--paper); font-size: 26px; letter-spacing: 1px;
  }
  .hero {
    position: absolute; left: 0; top: 86px; width: 620px; height: 355px;
  }
  .hero-photo {
    position: absolute; inset: 0;
    background:
      radial-gradient(ellipse at 78% 45%, rgba(230,210,170,0.55) 0%, rgba(230,210,170,0) 40%),
      linear-gradient(180deg, #d89a4e 0%, #b5602e 35%, #7a3218 62%, #2a120b 82%, #1a0b07 100%);
  }
  .hero-desk {
    position: absolute; left: 0; right: 0; bottom: 0; height: 110px;
    background: linear-gradient(170deg, rgba(0,0,0,0) 0%, rgba(150,80,40,0.55) 55%, rgba(200,120,60,0.55) 100%);
  }
  .hero-banner {
    position: absolute; left: 0; top: 85px; width: 300px; height: 69px;
  }
  .hero-title {
    position: absolute; left: 36px; top: 93px;
    font-family: "Cinzel", serif; font-weight: 500;
    color: var(--paper); font-size: 22px; line-height: 27px; letter-spacing: 0.6px;
    white-space: nowrap;
  }
  .hero-intro {
    position: absolute; left: 35px; top: 161px;
    font-family: "Open Sans", sans-serif; font-weight: 700;
    color: var(--paper); font-size: 16.5px; line-height: 22.2px;
    white-space: nowrap;
  }
  .approach {
    position: absolute; top: 441px; height: 342px;
  }
  .approach--old { left: 0; width: 311px; }
  .approach--new {
    left: 311px; width: 309px;
    background: linear-gradient(180deg, var(--panel-blue) 0%, #0f5594 60%, var(--panel-blue) 100%);
  }
  .approach-title {
    position: absolute; top: 31px;
    font-family: "Cinzel", serif; font-weight: 400;
    color: var(--accent-orange); font-size: 17.5px; letter-spacing: 0.3px;
  }
  .approach--old .approach-title { left: 23px; }
  .approach--new .approach-title { left: 25px; }
  .step-list {
    position: absolute; top: 54px; list-style: none;
    font-family: "Montserrat", sans-serif; font-weight: 500;
    font-size: 7.2px; line-height: 15.1px;
  }
  .approach--old .step-list { left: 23px; color: var(--ink); }
  .approach--new .step-list { left: 26px; color: var(--paper); }
  .step-list li { position: relative; padding-left: 12px; }
  .step-list li::before {
    content: "•"; position: absolute; left: 0; top: 0;
  }
  .terms-title {
    position: absolute; left: 23px; top: 262px;
    font-family: "Cinzel", serif; font-weight: 400;
    color: var(--accent-orange); font-size: 17px;
  }
  .terms-text {
    position: absolute; left: 35px; top: 283px; width: 260px;
    font-family: "Montserrat", sans-serif; font-weight: 500;
    color: var(--ink); font-size: 7.3px; line-height: 13px;
  }
  .contact {
    position: absolute; left: 0; top: 792px; width: 620px;
    text-align: center; font-family: "Montserrat", sans-serif; color: var(--ink);
  }
  .contact-phone {
    font-size: 15px; font-weight: 500; color: var(--accent-orange); line-height: 20px;
  }
  .contact-phone .quote { color: var(--ink); font-size: 12px; }
  .contact-line { font-size: 10.6px; font-weight: 500; line-height: 15px; }
</style>
</head>
<body>
  <main class="flyer">
    <header class="masthead">
      <span class="brand-name">MARRICK &amp; DACE LEGAL</span>
    </header>

    <section class="hero">
      <div class="hero-photo" role="img" aria-label="Photograph of brass scales of justice on a wooden courtroom desk with a warm blurred background"></div>
      <div class="hero-desk"></div>
      <svg class="hero-banner" viewBox="0 0 300 69" aria-hidden="true">
        <polygon points="0,0 272,0 300,69 0,69" fill="var(--accent-orange)"/>
      </svg>
      <h1 class="hero-title">FINALISING YOUR<br>DIVORCE MADE EASY</h1>
      <p class="hero-intro">Are you separated and both<br>seeking to Divorce?&nbsp; At Marrick<br>&amp; Dace Legal&nbsp; we provide a<br>cost effective way for this to occur</p>
    </section>

    <section class="approach approach--old">
      <h2 class="approach-title">OLD APPROACH</h2>
      <ul class="step-list">
        <li>Arrange a meeting with a solicitor</li>
        <li>Attend appointment</li>
        <li>Provide background information to the lawyer</li>
        <li>Lawyer to draft document</li>
        <li>Lawyer to contact you to obtain further instructions, if required</li>
        <li>Lawyer to amend divorce application, if further amendments</li>
        <li>required</li>
        <li>Lawyer to send you a copy of the draft Divorce Application</li>
        <li>Lawyer to make further changes, if required</li>
        <li>Lawyer to resend you draft Divorce Application, if required</li>
        <li>Lawyer to organise an appointment to attend office to sign</li>
        <li>Divorce Application</li>
        <li>TIME CONSUMING &amp; COSTLY - CAN COST OVER $3500</li>
      </ul>
      <h2 class="terms-title">TERMS &amp; CONDITIONS</h2>
      <p class="terms-text">Applies to simple joint divorce applications, no court appearances, no drafting or finalising any further court documentations, &amp; excludes disbursements costs including court filing fee</p>
    </section>

    <section class="approach approach--new">
      <h2 class="approach-title">NEW APPROACH</h2>
      <ul class="step-list">
        <li>We send you a Form</li>
        <li>You complete the Form</li>
        <li>We review your instructions</li>
        <li>We provide you with advice</li>
        <li>We draft Divorce Application and send to you for review</li>
        <li>QUICK &amp; SIMPLE PROCESS - FIXED COST OF $799</li>
        <li>INCLUSIVE OF GST</li>
      </ul>
    </section>

    <footer class="contact">
      <p class="contact-phone"><span class="quote">“</span> (08) 5550 2741 <span class="quote">”</span></p>
      <p class="contact-line">Melbourne Level 4/118 Harlow Street, MELBOURNE VIC 3000 03 5550 6182</p>
      <p class="contact-line">office@marrickanddacelegal.com.au</p>
      <p class="contact-line">www.marrickanddacelegal.com.au</p>
    </footer>
  </main>
</body>
</html>
```